sydney wedding photography business needs a business card design

we need a business card design for a sydney based wedding photography and videography business. our business name is :golden hour studios and film. our target clients are 24-35 yrs female. our style is candid, organic, natural, dynamic. we are a team of young photographers and videographers, and help brides to create memories that they will cherish for the rest of their lives. the logo will be provided. we want an elegant design that reflects our style, and also want to give a great impression to our clients that we are one of the best studios in sydney and our brand means quality and premium service.

Target Market(s)

bride to be, 24-35 years old, living in sydney and surrunding areas

Industry/Entity Type

Wedding Photography

Contact Information for Business Card

address: 47 marrowbank street, wrenfield nsw 2199
mobile: 0417283951
phone: (02) 9163 2748
info@goldenhourstudio.net.au
www.goldenhourstudio.net.au
facebook:goldenhourbridals
instagram:goldenhourbridals

Font styles to use
Serif
Sans Serif

Requirements
Nice to have
• maybe add my slogan"memories beyond eternity" if the layout looks good
Should not have
• no black color, not good idea for wedding biz card

```html
<!DOCTYPE html>
<html lang="en">
<head>
<meta charset="utf-8">
<title>Golden Hour Studios and Film – Business Card</title>
<link href="https://fonts.googleapis.com/css2?family=Arimo:wght@400&display=swap" rel="stylesheet">
<style>
  :root {
    --bg: #ece8e2;
    --card: #fbfbfa;
    --gold: #c9a93e;
    --ink: #2b2b2b;
    --band: rgba(205, 205, 210, 0.55);
    --brick-dark: #6b4a33;
    --brick: #a8835e;
    --veil: #e9e6f2;
  }
  * { box-sizing: border-box; margin: 0; padding: 0; }
  html, body { width: 1200px; height: 902px; overflow: hidden; }
  body {
    background: var(--bg);
    font-family: "Arimo", Arial, sans-serif;
    display: flex;
    flex-direction: column;
    align-items: center;
    justify-content: center;
    gap: 32px;
  }
  .card {
    width: 720px;
    height: 410px;
    position: relative;
    overflow: hidden;
    background: var(--card);
    box-shadow: 0 6px 18px rgba(60, 45, 30, 0.18);
  }

  /* Front */
  .card-front .photo {
    position: absolute;
    inset: 0;
    background:
      radial-gradient(ellipse 22% 38% at 54% 38%, #f4ede0 0%, rgba(244,237,224,0) 100%),
      linear-gradient(180deg, var(--brick-dark) 0%, var(--brick) 38%, #b9a892 62%, var(--veil) 82%, #f1f0f3 100%);
  }
  .card-front .band {
    position: absolute;
    left: 0; right: 0;
    top: 150px;
    height: 110px;
    background: var(--band);
    display: flex;
    flex-direction: column;
    align-items: center;
    justify-content: center;
  }
  .brand-name {
    color: var(--gold);
    font-weight: 400;
    font-size: 50px;
    line-height: 1;
    letter-spacing: 0.5px;
  }
  .brand-sub {
    color: var(--gold);
    font-weight: 400;
    font-size: 15px;
    letter-spacing: 9px;
    margin-top: 8px;
    text-transform: uppercase;
  }

  /* Back */
  .card-back .logo {
    position: absolute;
    left: 40px;
    top: 168px;
    width: 300px;
    text-align: center;
  }
  .card-back .brand-name { font-size: 40px; }
  .card-back .brand-sub { font-size: 12px; letter-spacing: 7px; }
  .divider {
    position: absolute;
    left: 372px;
    top: 70px;
    width: 2px;
    height: 270px;
    background: var(--gold);
  }
  .contact-list {
    position: absolute;
    left: 392px;
    top: 100px;
    list-style: none;
    color: var(--ink);
    font-size: 15px;
  }
  .contact-list li {
    display: flex;
    align-items: center;
    gap: 10px;
    height: 28px;
    white-space: nowrap;
  }
  .contact-list .icon {
    width: 16px;
    height: 16px;
    flex: none;
    background: var(--gold);
    display: flex;
    align-items: center;
    justify-content: center;
  }
  .contact-list .icon svg { width: 11px; height: 11px; }
</style>
</head>
<body>

  <section class="card card-front">
    <div class="photo" role="img" aria-label="Wedding couple embracing beneath a brick archway, bride's veil flowing"></div>
    <div class="band">
      <span class="brand-name">Golden Hour</span>
      <span class="brand-sub">Studios and Film</span>
    </div>
  </section>

  <section class="card card-back">
    <div class="logo">
      <div class="brand-name">Golden Hour</div>
      <div class="brand-sub">Studios and Film</div>
    </div>
    <div class="divider"></div>
    <ul class="contact-list">
      <li><span class="icon"><svg viewBox="0 0 12 12"><path d="M2.5 1l2 2-1 1.3c.6 1.4 1.8 2.6 3.2 3.2L8 6.5l2 2-1.2 1.8C5 10 2 7 1.7 3.2z" fill="#fff"/></svg></span>(02) 9163 2748</li>
      <li><span class="icon"><svg viewBox="0 0 12 12"><rect x="3.5" y="1" width="5" height="10" rx="1" fill="none" stroke="#fff" stroke-width="1.2"/><circle cx="6" cy="9.2" r=".6" fill="#fff"/></svg></span>0417283951</li>
      <li><span class="icon"><svg viewBox="0 0 12 12"><circle cx="6" cy="6" r="4.5" fill="none" stroke="#fff" stroke-width="1.1"/><path d="M1.5 6h9M6 1.5c-2 2.5-2 6.5 0 9M6 1.5c2 2.5 2 6.5 0 9" fill="none" stroke="#fff" stroke-width=".9"/></svg></span>www.goldenhourstudio.net.au</li>
      <li><span class="icon"><svg viewBox="0 0 12 12"><rect x="1.5" y="3" width="9" height="6" fill="none" stroke="#fff" stroke-width="1.1"/><path d="M1.5 3L6 6.5 10.5 3" fill="none" stroke="#fff" stroke-width="1.1"/></svg></span>info@goldenhourstudio.net.au</li>
      <li><span class="icon"></span>goldenhourbridals</li>
      <li><span class="icon"></span>goldenhourbridals</li>
      <li><span class="icon"><svg viewBox="0 0 12 12"><path d="M6 11S2.5 7 2.5 4.6a3.5 3.5 0 0 1 7 0C9.5 7 6 11 6 11z" fill="#fff"/><circle cx="6" cy="4.6" r="1.2" fill="#c9a93e"/></svg></span>47 marrowbank street, wrenfield nsw 2199</li>
    </ul>
  </section>

</body>
</html>
```